Direct mail campaign for roofing company

We are a roofing company looking to catch the eye of homeowners using direct mail post cards the are 6x9. We want to advertise that we are who to call for all your roofing needs. This need to be front and back
Crest Roofing
888.517.CRST
crestroofingpro.example

Target Market(s)

Single family homes

Industry/Entity Type

Roofing

Colors

Designer to choose colors to be used in the design.

```html
<!DOCTYPE html>
<html lang="en">
<head>
<meta charset="utf-8">
<title>Crest Roofing – Direct Mail Postcard</title>
<link rel="stylesheet" href="https://fonts.googleapis.com/css2?family=Montserrat:wght@500;600;700;800;900&display=swap">
<style>
  :root {
    --hive-yellow: #f2b01e;
    --ink: #141414;
    --paper: #ffffff;
    --stage: #e4e4e4;
    --stamp: #dcdcdc;
  }
  * { box-sizing: border-box; margin: 0; padding: 0; }
  html, body { width: 1200px; height: 2380px; overflow: hidden; }
  body {
    background: var(--stage);
    font-family: "Montserrat", Arial, sans-serif;
    color: var(--ink);
    position: relative;
  }
  .postcard {
    position: absolute;
    left: 50px;
    width: 1100px;
    height: 733px;
    overflow: hidden;
    box-shadow: 0 6px 20px rgba(0,0,0,.18);
  }
  .postcard--front { top: 407px; background: var(--hive-yellow); }
  .postcard--back { top: 1240px; background: var(--paper); }

  /* ---------- FRONT ---------- */
  .front-topband {
    position: absolute; left: 0; top: 0; width: 100%; height: 140px;
    background: var(--ink);
  }
  .brand {
    position: absolute; display: flex; align-items: center; gap: 14px;
    font-weight: 700; letter-spacing: .5px; text-transform: uppercase; white-space: nowrap;
  }
  .brand__mark { width: 34px; height: 34px; border: 4px solid var(--hive-yellow); }
  .front .brand { right: 50px; top: 50px; color: var(--hive-yellow); font-size: 22px; }
  .honeycomb { position: absolute; left: 0; top: 0; width: 620px; height: 733px; }
  .front-copy {
    position: absolute; left: 640px; top: 175px; width: 420px;
  }
  .front-copy__lead {
    font-weight: 800; font-size: 29px; line-height: 1.12; text-transform: uppercase; white-space: nowrap;
  }
  .front-copy__protect {
    font-weight: 900; font-size: 78px; line-height: 1; margin-top: 12px; letter-spacing: -1px; white-space: nowrap;
  }
  .front-copy__your {
    font-weight: 900; font-size: 52px; line-height: 1.05; color: var(--paper); letter-spacing: -1px; white-space: nowrap;
  }
  .values-bar {
    margin-top: 16px; background: var(--ink); color: var(--paper);
    font-weight: 800; font-size: 19px; letter-spacing: 1px; white-space: nowrap;
    padding: 10px 12px; text-align: center;
  }
  .cta-bar {
    position: absolute; left: 640px; right: 0; top: 560px;
    background: var(--ink); color: var(--hive-yellow); white-space: nowrap;
    font-weight: 800; font-size: 20px; padding: 14px 20px; letter-spacing: .5px;
  }
  .phone-line {
    position: absolute; display: flex; align-items: center; gap: 14px;
    font-weight: 900; letter-spacing: 1px; white-space: nowrap;
  }
  .front .phone-line { left: 644px; top: 632px; font-size: 44px; }

  /* ---------- BACK ---------- */
  .services-title {
    position: absolute; left: 48px; top: 42px;
    color: var(--hive-yellow); font-weight: 900; font-size: 38px;
  }
  .services-rule {
    position: absolute; left: 48px; top: 92px; width: 560px; height: 3px; background: var(--hive-yellow);
  }
  .services {
    position: absolute; left: 48px; top: 118px; width: 600px; list-style: none;
    display: grid; grid-template-columns: 1fr 1fr; row-gap: 24px; column-gap: 20px;
  }
  .service { display: flex; align-items: center; gap: 14px; font-weight: 700; font-size: 19px; line-height: 1.2; }
  .service__icon { width: 54px; height: 60px; flex: none; }
  .serving { position: absolute; left: 48px; top: 300px; width: 172px; }
  .serving__label { color: var(--hive-yellow); font-weight: 800; font-size: 20px; }
  .serving__area { font-weight: 800; font-size: 19px; line-height: 1.15; margin-top: 4px; text-transform: uppercase; }
  .back-photo {
    position: absolute; left: 230px; top: 285px; width: 430px; height: 295px;
    background: linear-gradient(180deg, #b9cde0 0%, #8fa3b5 38%, #6b6e72 58%, #2f3e55 78%, #4a4a48 100%);
  }
  .back-cta {
    position: absolute; left: 0; top: 580px; width: 660px; height: 66px;
    background: var(--hive-yellow); color: var(--paper); white-space: nowrap;
    font-weight: 900; font-size: 25px; line-height: 66px; padding: 0 48px; letter-spacing: .5px;
  }
  .back-contact {
    position: absolute; left: 0; top: 646px; width: 660px; height: 87px;
    background: var(--ink); color: var(--paper);
  }
  .back .phone-line { left: 48px; top: 22px; font-size: 34px; color: var(--paper); }
  .back-contact__web {
    position: absolute; right: 24px; top: 35px; font-weight: 600; font-size: 14px; color: var(--paper); white-space: nowrap;
  }
  .stamp-box {
    position: absolute; right: 48px; top: 42px; width: 110px; height: 130px; background: var(--stamp);
  }
  .back .brand { right: 60px; bottom: 60px; color: var(--ink); font-size: 18px; }
</style>
</head>
<body>

<section class="postcard postcard--front front">
  <div class="front-topband"></div>

  <svg class="honeycomb" viewBox="0 0 620 733" xmlns="http://www.w3.org/2000/svg">
    <defs>
      <linearGradient id="roofGrad" x1="0" y1="0" x2="0" y2="1">
        <stop offset="0" stop-color="#c9d6e3"/><stop offset=".45" stop-color="#8d8f92"/><stop offset="1" stop-color="#4f5b47"/>
      </linearGradient>
      <linearGradient id="houseGrad" x1="0" y1="0" x2="0" y2="1">
        <stop offset="0" stop-color="#a9c3dc"/><stop offset=".5" stop-color="#6d6a66"/><stop offset="1" stop-color="#5c6b3f"/>
      </linearGradient>
      <linearGradient id="shingleGrad" x1="0" y1="0" x2="1" y2="1">
        <stop offset="0" stop-color="#9aa3ab"/><stop offset="1" stop-color="#5a5e62"/>
      </linearGradient>
    </defs>
    <g stroke="#141414" stroke-width="12" stroke-linejoin="round">
      <polygon role="img" aria-label="Photo: large two-storey house with new grey roof" fill="url(#houseGrad)" points="330,210 460,285 460,435 330,510 200,435 200,285"/>
      <polygon role="img" aria-label="Photo: roofer working on a rooftop" fill="url(#roofGrad)" points="140,105 222,152 222,248 140,295 58,248 58,152"/>
      <polygon role="img" aria-label="Photo: crew installing shingles" fill="url(#shingleGrad)" points="100,320 169,360 169,440 100,480 31,440 31,360"/>
      <polygon role="img" aria-label="Photo: close-up of finished shingle roof" fill="url(#shingleGrad)" points="250,510 337,560 337,660 250,710 163,660 163,560"/>
      <polygon role="img" aria-label="Photo: brick home at dusk" fill="url(#houseGrad)" points="540,380 618,425 618,515 540,560 462,515 462,425"/>
      <polygon role="img" aria-label="Photo: roof ridge against blue sky" fill="url(#roofGrad)" points="470,70 539,110 539,190 470,230 401,190 401,110"/>
    </g>
  </svg>

  <div class="brand"><span class="brand__mark"></span><span>crestroofingpro.example</span></div>

  <div class="front-copy">
    <p class="front-copy__lead">You worked hard<br>building your home.</p>
    <p class="front-copy__protect">PROTECT</p>
    <p class="front-copy__your">YOUR CREST!</p>
    <p class="values-bar">TRUSTD | LOCAL | FAMILY OWNED</p>
  </div>

  <p class="cta-bar">CALL FOR ALL YOUR ROOFING NEEDS</p>
  <p class="phone-line">
    <svg width="40" height="40" viewBox="0 0 24 24" aria-hidden="true"><path fill="#141414" d="M6.6 10.8a15.1 15.1 0 0 0 6.6 6.6l2.2-2.2c.3-.3.7-.4 1-.2 1.1.4 2.3.6 3.6.6.6 0 1 .4 1 1V20c0 .6-.4 1-1 1A17 17 0 0 1 3 4c0-.6.4-1 1-1h3.5c.6 0 1 .4 1 1 0 1.3.2 2.5.6 3.6.1.3 0 .7-.2 1z"/></svg>
    <span>888.517.CRST</span>
  </p>
</section>

<section class="postcard postcard--back back">
  <h2 class="services-title">OUR SERVICES</h2>
  <div class="services-rule"></div>

  <ul class="services">
    <li class="service">
      <svg class="service__icon" viewBox="0 0 54 60" aria-hidden="true"><polygon points="27,2 52,16 52,44 27,58 2,44 2,16" fill="#f2b01e"/><path d="M15 32 27 21 39 32M19 30v11h16V30" fill="none" stroke="#fff" stroke-width="3"/></svg>
      <span>Retail/Commercial<br>Roof Replacement</span>
    </li>
    <li class="service">
      <svg class="service__icon" viewBox="0 0 54 60" aria-hidden="true"><polygon points="27,2 52,16 52,44 27,58 2,44 2,16" fill="#f2b01e"/><path d="M29 16 20 32h8l-3 12 10-17h-8z" fill="#fff"/></svg>
      <span>Storm Damage<br>Roof Replacement</span>
    </li>
    <li class="service">
      <svg class="service__icon" viewBox="0 0 54 60" aria-hidden="true"><polygon points="27,2 52,16 52,44 27,58 2,44 2,16" fill="#f2b01e"/><path d="M14 40h26M18 40V26h18v14M23 40v-8h8v8" fill="none" stroke="#fff" stroke-width="3"/></svg>
      <span>New Construction</span>
    </li>
    <li class="service">
      <svg class="service__icon" viewBox="0 0 54 60" aria-hidden="true"><polygon points="27,2 52,16 52,44 27,58 2,44 2,16" fill="#f2b01e"/><path d="M18 41 32 27M30 19a6 6 0 0 0 7 8l-3-3z" fill="none" stroke="#fff" stroke-width="3.5" stroke-linecap="round"/></svg>
      <span>Repairs &amp; Restoration</span>
    </li>
  </ul>

  <div class="serving">
    <p class="serving__label">SERVING</p>
    <p class="serving__area">North Georgia &amp; surrounding areas</p>
  </div>

  <div class="back-photo" role="img" aria-label="Photo: dark blue pickup truck parked in front of a newly roofed townhouse"></div>

  <p class="back-cta">CALL FOR ALL YOUR ROOFING NEEDS</p>
  <div class="back-contact">
    <p class="phone-line">
      <svg width="32" height="32" viewBox="0 0 24 24" aria-hidden="true"><path fill="#f2b01e" d="M6.6 10.8a15.1 15.1 0 0 0 6.6 6.6l2.2-2.2c.3-.3.7-.4 1-.2 1.1.4 2.3.6 3.6.6.6 0 1 .4 1 1V20c0 .6-.4 1-1 1A17 17 0 0 1 3 4c0-.6.4-1 1-1h3.5c.6 0 1 .4 1 1 0 1.3.2 2.5.6 3.6.1.3 0 .7-.2 1z"/></svg>
      <span>888.517.CRST</span>
    </p>
    <p class="back-contact__web">www.crestroofingpro.example</p>
  </div>

  <div class="stamp-box"></div>

  <div class="brand"><span class="brand__mark"></span><span>crestroofingpro.example</span></div>
</section>

</body>
</html>
```